Marketing based tech company needs infographics

I need an infographic created about our process as it pertains to event organizers working with marketers, marketers working with event organizers and both working with sponsors.

3 sections
Event Organizers Steps: Total Timeline 3-10 days
1. Event organizer submits their deck (proposal)
2. It is sent to a vetter for review
3. The vetter provides edits
4. The event organizer approves the edits
5. The deck is turned into a website link
6. The deck is ready for the event organizer to send to sponsors
7. Sponsors open it and are wowed!
Marketer Steps: Total timeline 3-10 days
1. the marketer receives the deck
2. Provides feedback/edits to the event organizer
3. The event organizer approves the edits
6. The vetter is paid for their work immediately after the website goes live
Sponsors Steps: Total Timeline 30+ days
1. Sponsor is matched only with events that meet their demographics.
2. Event organizer submits their deck (proposal) to sponsor
3. The sponsor reviews the deck
4. If they are wowed they continue the conversation.
5. The event terms are negotiated.
6. The event organizer is paid 14 days prior to the event.
7. The event happens and is a success!

Target Market(s)

Minority-owned businesses and event planners.

Industry/Entity Type

Marketing

Font styles to use
Sans Serif

Colors
f78f20
0455a3
0692cd

Requirements
Must have
• 3 sections
• Event Organizers Steps: Total Timeline 3-10 days
• 1. Event organizer submits their deck (proposal)
• 2. It is sent to a vetter for review
• 3. The vetter provides edits
• 4. The event organizer approves the edits
• 5. The deck is turned into a website link
• 6. The deck is ready for the event organizer to send to sponsors
• 7. Sponsors open it and are wowed!
• Marketer Steps: Total timeline 3-10 days
• 1. the marketer receives the deck
• 2. Provides feedback/edits to the event organizer
• 3. The event organizer approves the edits
• 6. The vetter is paid for their work immediately after the website goes live
• Sponsors Steps: Total Timeline 30+ days
• 1. Sponsor is matched only with events that meet their demographics.
• 2. Event organizer submits their deck (proposal) to sponsor
• 3. The sponsor reviews the deck
• 4. If they are wowed they continue the conversation.
• 5. The event terms are negotiated.
• 6. The event organizer is paid 14 days prior to the event.
• 7. The event happens and is a success!
Nice to have
• To incorporate the styles of the graphics and icons attached
Should not have
• Be creative!

```html
<!DOCTYPE html>
<html lang="en">
<head>
<meta charset="utf-8">
<title>Marketing Based Tech Company — Our Process</title>
<link href="https://fonts.googleapis.com/css2?family=Oswald:wght@400;500;600;700&family=Roboto+Condensed:wght@400;700&display=swap" rel="stylesheet">
<style>
  :root{
    --orange:#f78f20;
    --navy:#0455a3;
    --sky:#0692cd;
    --ink:#111111;
    --white:#ffffff;
    --mist:#eef1f4;
  }
  *{margin:0;padding:0;box-sizing:border-box}
  html,body{width:1200px;height:3838px;overflow:hidden;background:var(--white)}
  body{position:relative;font-family:"Roboto Condensed",Arial,sans-serif;color:var(--white)}
  .layer{position:absolute;left:0;top:0}
  .abs{position:absolute}

  /* header */
  .title-main{left:0;width:1200px;top:70px;text-align:center;font-family:Oswald,sans-serif;font-weight:700;font-size:104px;line-height:1;color:var(--orange);letter-spacing:1px}
  .title-sub{left:0;width:1200px;top:190px;text-align:center;font-family:Oswald,sans-serif;font-weight:400;font-size:62px;line-height:1;color:var(--white);letter-spacing:20px}
  .our-process{left:0;width:1200px;top:334px;text-align:center;font-family:Oswald,sans-serif;font-weight:500;font-size:50px;line-height:1;color:var(--ink);letter-spacing:12px}
  .step-head{font-family:Oswald,sans-serif;color:var(--white);text-align:center;line-height:.95}
  .step-head .big{display:block;font-weight:600;font-size:96px}
  .step-head .small{display:block;font-weight:500;font-size:38px}
  .timeline-bar{left:115px;top:818px;width:972px;height:78px;background:var(--orange);display:flex;align-items:center;justify-content:center;gap:24px;font-family:Oswald,sans-serif;font-weight:500;font-size:25px;color:var(--white)}

  /* event organizer section */
  .sections-heading{left:84px;top:1018px;height:90px;display:flex;align-items:center;gap:16px;padding:0 8px;white-space:nowrap}
  .sections-title{font-family:Oswald,sans-serif;font-weight:700;font-size:72px;line-height:1;color:var(--white);letter-spacing:-0.5px}
  .sections-lead{font-family:Oswald,sans-serif;font-weight:500;font-size:35px;line-height:1;color:var(--white)}
  .sections-lead small{display:block;font-family:"Roboto Condensed",sans-serif;font-weight:400;font-size:19px;margin-top:4px}
  .eo-label{left:28px;top:1410px;font-family:Oswald,sans-serif;line-height:1;color:var(--white)}
  .eo-label .big{display:block;font-weight:400;font-size:92px}
  .eo-label .small{display:block;font-weight:400;font-size:36px;margin-top:6px}
  .eo-step{font-size:25px;line-height:1;color:var(--white);white-space:nowrap}

  /* marketer section */
  .mk-label{left:38px;height:44px;background:var(--orange);color:var(--white);font-size:24px;font-weight:700;display:flex;align-items:center;padding-left:12px;white-space:nowrap}
  .mk-center{left:883px;top:2218px;width:230px;height:230px;border-radius:50%;display:flex;flex-direction:column;align-items:center;justify-content:center;font-family:Oswald,sans-serif;font-size:40px;line-height:1.1;color:var(--ink);text-align:center}

  /* sponsors section */
  .sp-step{font-size:23px;line-height:1.2;color:var(--white)}
  .sp-right{text-align:right}
  .sp-center{left:461px;top:3186px;width:280px;height:280px;display:flex;flex-direction:column;align-items:center;justify-content:center;font-family:Oswald,sans-serif;font-size:50px;line-height:1.1;color:var(--ink);text-align:center}
</style>
</head>
<body>

<!-- header shapes -->
<svg class="layer" width="1200" height="960" viewBox="0 0 1200 960">
  <polygon points="0,0 1200,0 1200,300 1120,318 80,318 0,300" fill="var(--ink)"/>
  <polygon points="30,322 210,412 990,412 1170,322 1170,830 30,830" fill="var(--navy)"/>
  <polygon points="384,412 820,412 601,832" fill="var(--sky)"/>
  <line x1="601" y1="832" x2="601" y2="945" stroke="var(--orange)" stroke-width="3"/>
  <circle cx="601" cy="832" r="10" fill="var(--white)" stroke="var(--orange)" stroke-width="3"/>
  <!-- calendar icon -->
  <circle cx="200" cy="558" r="40" fill="var(--white)"/>
  <rect x="182" y="544" width="36" height="32" rx="3" fill="none" stroke="var(--navy)" stroke-width="4"/>
  <line x1="182" y1="554" x2="218" y2="554" stroke="var(--navy)" stroke-width="4"/>
  <line x1="190" y1="538" x2="190" y2="548" stroke="var(--navy)" stroke-width="4"/>
  <line x1="210" y1="538" x2="210" y2="548" stroke="var(--navy)" stroke-width="4"/>
  <!-- megaphone icon -->
  <circle cx="601" cy="672" r="42" fill="var(--white)"/>
  <polygon points="580,662 592,662 618,646 618,698 592,682 580,682" fill="var(--sky)"/>
  <line x1="626" y1="664" x2="634" y2="660" stroke="var(--sky)" stroke-width="4"/>
  <line x1="626" y1="680" x2="634" y2="684" stroke="var(--sky)" stroke-width="4"/>
  <!-- handshake icon -->
  <circle cx="950" cy="558" r="40" fill="var(--white)"/>
  <path d="M926 560 l14 -12 h14 l10 8 l12 -8 M926 560 l18 16 q6 4 12 0 l20 -16" fill="none" stroke="var(--navy)" stroke-width="5" stroke-linejoin="round"/>
</svg>

<div class="abs title-main">MARKETING BASED</div>
<div class="abs title-sub">TECH COMPANY</div>
<div class="abs our-process">OUR PROCESS</div>
<div class="abs step-head" style="left:460px;top:450px;width:282px"><span class="small" style="font-size:40px">MARKETER</span><span class="big" style="font-size:90px">STEP</span></div>
<div class="abs step-head" style="left:120px;top:624px;width:300px;text-align:left"><span class="big">EVENT</span><span class="small" style="font-size:30px">ORGANIZERS STEP</span></div>
<div class="abs step-head" style="left:800px;top:618px;width:300px"><span class="small">SPONSORS</span><span class="big">STEP</span></div>
<div class="abs timeline-bar"><span>TOTAL TIMELINE 3-10 DAYS</span><span>—</span><span>TOTAL TIMELINE 3-10 DAYS</span><span>—</span><span>TOTAL TIMELINE 30+ DAYS</span></div>

<!-- event organizers section -->
<svg class="layer" style="top:0" width="1200" height="2000" viewBox="0 0 1200 2000">
  <defs>
    <linearGradient id="blueFade" x1="0" y1="0" x2="0" y2="1">
      <stop offset="0" stop-color="var(--sky)"/>
      <stop offset="1" stop-color="var(--navy)"/>
    </linearGradient>
  </defs>
  <polygon points="0,934 1200,934 1200,1830 601,1957 0,1830" fill="url(#blueFade)"/>
  <circle cx="601" cy="944" r="14" fill="var(--white)" stroke="var(--orange)" stroke-width="3"/>
  <polyline points="30,1018 30,1108 1170,1108 1170,1018 1125,1018" fill="none" stroke="var(--white)" stroke-width="3"/>
  <line x1="30" y1="1018" x2="75" y2="1018" stroke="var(--white)" stroke-width="3"/>
  <path d="M58 1185 A305 305 0 0 1 58 1795" fill="none" stroke="var(--white)" stroke-width="3"/>
  <g fill="var(--orange)" stroke="var(--white)" stroke-width="3">
    <circle cx="161" cy="1203" r="12"/><circle cx="290" cy="1292" r="12"/><circle cx="348" cy="1394" r="12"/>
    <circle cx="363" cy="1492" r="12"/><circle cx="346" cy="1591" r="12"/><circle cx="289" cy="1689" r="12"/>
    <circle cx="172" cy="1773" r="12"/>
  </g>
  <g fill="var(--navy)" stroke="var(--white)" stroke-width="3">
    <circle cx="276" cy="1203" r="24"/><circle cx="420" cy="1292" r="24"/><circle cx="478" cy="1394" r="24"/>
    <circle cx="495" cy="1492" r="24"/><circle cx="476" cy="1591" r="24"/><circle cx="419" cy="1689" r="24"/>
    <circle cx="276" cy="1773" r="24"/>
  </g>
  <g fill="none" stroke="var(--white)" stroke-width="3" stroke-linecap="round">
    <rect x="267" y="1192" width="18" height="22" rx="2"/>
    <path d="M412 1284 h12 l4 4 v14 h-16z"/>
    <path d="M468 1400 h20 M472 1392 h12 M476 1384 h6"/>
    <path d="M485 1486 l6 6 l12 -12 M485 1500 h18"/>
    <path d="M466 1591 a10 10 0 1 0 10 -10 l-4 -4 M476 1581 l-4 4"/>
    <path d="M407 1692 l8 -7 h8 l6 5 l7 -5 M407 1692 l10 9 q3 2 6 0 l12 -9"/>
    <circle cx="276" cy="1766" r="5"/><path d="M265 1784 q11 -12 22 0"/>
  </g>
</svg>

<div class="abs sections-heading">
  <div class="sections-title">3 SECTIONS</div>
  <div class="sections-lead">EVENT ORGANIZERS WORKING WITH MARKETERS,<small>Marketers working with event organizers, Both working with sponsors</small></div>
</div>
<div class="abs eo-label"><span class="big">EVENT</span><span class="small">ORGANIZERS STEPS</span></div>
<div class="abs eo-step" style="left:345px;top:1191px">Event organizer submits their deck (proposal).</div>
<div class="abs eo-step" style="left:488px;top:1280px">It is sent to a vetter for review.</div>
<div class="abs eo-step" style="left:546px;top:1382px">The vetter provides edits.</div>
<div class="abs eo-step" style="left:563px;top:1480px">The event organizer approves the edits.</div>
<div class="abs eo-step" style="left:544px;top:1579px">The deck is turned into a website link.</div>
<div class="abs eo-step" style="left:487px;top:1677px">The deck is ready for the event organizer to send to sponsors.</div>
<div class="abs eo-step" style="left:345px;top:1761px">Sponsors open it and are wowed!.</div>

<!-- marketer section -->
<div class="abs" role="img" aria-label="Faint world map backdrop" style="left:60px;top:2000px;width:1120px;height:780px;background:radial-gradient(ellipse at center,var(--mist),rgba(238,241,244,0) 72%)"></div>
<svg class="layer" width="1200" height="3838" viewBox="0 0 1200 3838">
  <polygon points="580,1975 601,1990 622,1975" fill="none" stroke="var(--orange)" stroke-width="4"/>
  <g fill="none" stroke="var(--orange)" stroke-width="3">
    <polyline points="435,2039 1077,2039 1077,2171"/>
    <polyline points="601,2149 922,2149 922,2170"/>
    <polyline points="576,2292 823,2292"/>
    <polyline points="486,2425 856,2425 856,2444"/>
    <polyline points="993,2558 978,2558 978,2512"/>
    <polyline points="768,2663 1100,2663 1100,2481"/>
    <polyline points="422,2768 1175,2768 1175,2366"/>
  </g>
  <g transform="translate(998 2333)">
    <circle r="180" fill="var(--orange)"/>
    <g stroke="var(--white)" stroke-width="7">
      <line x1="0" y1="0" x2="186" y2="0" transform="rotate(-38.3)"/>
      <line x1="0" y1="0" x2="186" y2="0" transform="rotate(-89.7)"/>
      <line x1="0" y1="0" x2="186" y2="0" transform="rotate(-141.3)"/>
      <line x1="0" y1="0" x2="186" y2="0" transform="rotate(167.3)"/>
      <line x1="0" y1="0" x2="186" y2="0" transform="rotate(115.9)"/>
      <line x1="0" y1="0" x2="186" y2="0" transform="rotate(64.5)"/>
      <line x1="0" y1="0" x2="186" y2="0" transform="rotate(13)"/>
    </g>
    <circle r="118" fill="var(--white)"/>
    <g font-family="Roboto Condensed, sans-serif" font-size="24" fill="var(--white)" text-anchor="middle" dominant-baseline="middle">
      <text x="65" y="-133">1</text><text x="-63" y="-134">2</text><text x="-144" y="-33">3</text>
      <text x="-117" y="91">4</text><text x="-2" y="148">5</text><text x="115" y="93">6</text><text x="145" y="-31">7</text>
    </g>
  </g>
</svg>
<div class="abs mk-center"><span>MARKETER</span><span>STEPS</span></div>
<div class="abs mk-label" style="top:2017px;width:397px">The marketer receives the deck</div>
<div class="abs mk-label" style="top:2127px;width:563px">Provides feedback/edits to the event organizer</div>
<div class="abs mk-label" style="top:2270px;width:538px">The event organizer approves the edits</div>
<div class="abs mk-label" style="top:2403px;width:448px">The deck is turned into a website link</div>
<div class="abs mk-label" style="top:2536px;width:955px">The vetter is paid for their work immediately after the website goes live</div>
<div class="abs mk-label" style="top:2641px;width:730px">The deck is ready for the event organizer to send to sponsors</div>
<div class="abs mk-label" style="top:2746px;width:384px">Spoansors open it and are wowed!</div>

<!-- sponsors section -->
<svg class="layer" width="1200" height="3838" viewBox="0 0 1200 3838">
  <defs>
    <linearGradient id="blueFade2" x1="0" y1="0" x2="0" y2="1">
      <stop offset="0" stop-color="var(--sky)"/>
      <stop offset="1" stop-color="var(--navy)"/>
    </linearGradient>
  </defs>
  <rect x="0" y="2828" width="1200" height="1010" fill="url(#blueFade2)"/>
  <polyline points="582,2908 601,2920 620,2908" fill="none" stroke="var(--navy)" stroke-width="5"/>
  <g stroke="var(--white)" stroke-width="3">
    <line x1="601" y1="3326" x2="530" y2="3014"/><line x1="601" y1="3326" x2="768" y2="3040"/>
    <line x1="601" y1="3326" x2="934" y2="3237"/><line x1="601" y1="3326" x2="921" y2="3441"/>
    <line x1="601" y1="3326" x2="806" y2="3608"/><line x1="601" y1="3326" x2="635" y2="3654"/>
    <line x1="601" y1="3326" x2="430" y2="3628"/><line x1="601" y1="3326" x2="284" y2="3480"/>
    <line x1="601" y1="3326" x2="269" y2="3275"/><line x1="601" y1="3326" x2="333" y2="3109"/>
  </g>
  <polygon points="528,3150 674,3150 777,3253 777,3399 674,3502 528,3502 425,3399 425,3253" fill="var(--white)" stroke="var(--orange)" stroke-width="6"/>
  <g fill="var(--white)" stroke="var(--orange)" stroke-width="5">
    <circle cx="530" cy="3014" r="38"/><circle cx="768" cy="3040" r="38"/><circle cx="934" cy="3237" r="38"/>
    <circle cx="921" cy="3441" r="38"/><circle cx="806" cy="3608" r="38"/><circle cx="635" cy="3654" r="38"/>
    <circle cx="430" cy="3628" r="38"/><circle cx="284" cy="3480" r="38"/><circle cx="269" cy="3275" r="38"/>
    <circle cx="333" cy="3109" r="38"/>
  </g>
  <g fill="none" stroke="var(--navy)" stroke-width="3.5" stroke-linecap="round" stroke-linejoin="round">
    <path d="M519 3000 h22 v28 h-22z M524 3010 h12 M524 3018 h12"/>
    <path d="M752 3042 l10 -9 h10 l8 6 l8 -6 M752 3042 l13 12 q4 3 8 0 l15 -12"/>
    <circle cx="926" cy="3228" r="6"/><path d="M914 3250 q12 -14 24 0 M940 3232 h12 v16 h-12"/>
    <circle cx="912" cy="3436" r="5"/><circle cx="930" cy="3436" r="5"/><path d="M902 3456 q10 -12 20 0 M920 3456 q10 -12 20 0"/>
    <path d="M790 3598 h32 v18 h-18 l-8 7 v-7 h-6z"/>
    <path d="M620 3640 h30 v28 h-30z M626 3654 l6 6 l12 -12"/>
    <path d="M414 3614 h32 v28 h-32z M414 3624 h32 M422 3634 h8"/>
    <path d="M270 3468 h26 v24 h-26z M277 3482 l5 5 l8 -9"/>
    <path d="M280 3263 a12 12 0 1 1 -10 -2 M270 3261 l4 -6 M270 3261 l6 4"/>
    <path d="M320 3100 h26 v18 h-26z M326 3094 h14 M330 3124 h6"/>
  </g>
</svg>
<div class="abs sp-center"><span>SPONSORS</span><span>STEPS</span></div>
<div class="abs sp-step" style="left:98px;top:2980px;width:380px;text-align:right">Sponsors open it and are wowed!</div>
<div class="abs sp-step" style="left:840px;top:2986px;width:340px">Sponsor is matched only with events that meet their demographics.</div>
<div class="abs sp-step" style="left:996px;top:3164px;width:170px">Event organizer submits their deck (proposal) to sponsor</div>
<div class="abs sp-step" style="left:984px;top:3420px;width:190px">The sponsor reviews the deck</div>
<div class="abs sp-step" style="left:862px;top:3594px;width:320px">If they are wowed they continue the conversation</div>
<div class="abs sp-step" style="left:435px;top:3704px;width:400px;text-align:center">The event terms are negotiated</div>
<div class="abs sp-step sp-right" style="left:20px;top:3598px;width:360px">The event organizer is paid 14 days prior to the event</div>
<div class="abs sp-step sp-right" style="left:60px;top:3436px;width:176px">The event happens and is a success!</div>
<div class="abs sp-step sp-right" style="left:60px;top:3232px;width:164px">The deck is turned into a website link</div>
<div class="abs sp-step sp-right" style="left:30px;top:3060px;width:252px">The deck is ready for the event organizer to send to sponsors</div>

</body>
</html>
```